Business Card Design

We are looking for a business card designed for our landscaping company. We do landscaping installation & Maintenance Services. We would like to see designs that have basic landscaping in background. We also think it is important to have both of our names and phone numbers on the card. We need something that stands out a little whether it is shape of the card or thickness or design.

Industry/Entity Type

Business

Contact Information for Business Card

Pale Ridge Yardworks, paleridgeyardworks@mailbrook.net, Dale Purvine 555-213-7690, Martin Kolbey 555-864-1037

```html
<!DOCTYPE html>
<html lang="en">
<head>
<meta charset="utf-8">
<title>Pale Ridge Yardworks – Business Card</title>
<link rel="stylesheet" href="https://fonts.googleapis.com/css2?family=Roboto+Condensed:wght@700&family=Roboto:wght@400&display=swap">
<style>
  :root {
    --grass-light: #7cc043;
    --grass-mid: #4f9a2a;
    --grass-dark: #2f6f1a;
    --band-grey: #8e8e8e;
    --band-grey-light: #a6a6a6;
    --panel-white: #ffffff;
    --ink: #3a3a3a;
    --title-white: #ffffff;
    --leaf-green: #6bb23a;
  }
  html, body {
    margin: 0;
    padding: 0;
    width: 1200px;
    height: 672px;
    overflow: hidden;
    background: #ffffff;
  }
  .card {
    position: relative;
    width: 1200px;
    height: 672px;
    overflow: hidden;
    font-family: "Roboto", Arial, sans-serif;
  }
  .grass-field {
    position: absolute;
    inset: 0;
    background:
      radial-gradient(ellipse at 30% 40%, var(--grass-light) 0%, transparent 60%),
      linear-gradient(160deg, var(--grass-mid) 0%, var(--grass-light) 45%, var(--grass-mid) 75%, var(--grass-dark) 100%);
  }
  .corner-band {
    position: absolute;
    left: 706px;
    top: 0;
    width: 494px;
    height: 68px;
    background: linear-gradient(90deg, var(--band-grey-light), var(--band-grey));
  }
  .company-name {
    position: absolute;
    left: 0;
    width: 708px;
    margin: 0;
    text-align: center;
    font-family: "Roboto Condensed", "Arial Narrow", sans-serif;
    font-weight: 700;
    font-size: 112px;
    line-height: 115px;
    color: var(--title-white);
    top: 158px;
    letter-spacing: 1px;
  }
  .divider {
    position: absolute;
    left: 30px;
    top: 411px;
    width: 639px;
    height: 2px;
    background: var(--title-white);
  }
  .services {
    position: absolute;
    left: 0;
    top: 458px;
    width: 708px;
    margin: 0;
    text-align: center;
    font-size: 37px;
    line-height: 48px;
    color: var(--title-white);
    letter-spacing: 1px;
  }
  .contact-panel {
    position: absolute;
    left: 702px;
    top: 130px;
    width: 498px;
    height: 443px;
    background: var(--panel-white);
  }
  .leaf-icon {
    position: absolute;
  }
  .contact-name, .contact-phone, .contact-email {
    position: absolute;
    margin: 0;
    white-space: nowrap;
    color: var(--ink);
  }
  .contact-name { font-size: 33px; line-height: 40px; }
  .contact-phone { font-size: 39px; line-height: 46px; letter-spacing: 1px; }
  .contact-email { font-size: 27px; line-height: 34px; }
</style>
</head>
<body>
<div class="card">
  <div class="grass-field" role="img" aria-label="Close-up of lush green lawn grass"></div>
  <div class="corner-band"></div>

  <h1 class="company-name">Pale Ridge<br>Yardworks</h1>
  <div class="divider"></div>
  <p class="services">landscaping installation &amp;<br>Maintenance Services</p>

  <div class="contact-panel"></div>

  <svg class="leaf-icon" style="left:738px;top:185px" width="72" height="48" viewBox="0 0 72 48" role="img" aria-label="Green leaf icon">
    <ellipse cx="36" cy="24" rx="30" ry="18" fill="var(--leaf-green)"/>
  </svg>
  <p class="contact-name" style="left:818px;top:196px">Dale Purvine</p>
  <p class="contact-phone" style="left:757px;top:246px">555-213-7690</p>

  <svg class="leaf-icon" style="left:751px;top:340px" width="66" height="68" viewBox="0 0 66 68" role="img" aria-label="Green leaf icon">
    <ellipse cx="33" cy="34" rx="26" ry="28" fill="var(--leaf-green)"/>
  </svg>
  <p class="contact-name" style="left:818px;top:370px">Martin Kolbey</p>
  <p class="contact-phone" style="left:757px;top:422px">555-864-1037</p>

  <p class="contact-email" style="left:757px;top:503px">paleridgeyardworks@mailbrook.net</p>
</div>
</body>
</html>
```